Business Card Design Project

I have attached the logo and the colour pallete for the branding for the company.

Creative designs for business cards are needed.

The Company is modern corporate.

Industry/Entity Type

Business

```html
<!DOCTYPE html>
<html lang="en">
<head>
<meta charset="utf-8">
<title>Stepwise — Business Card Set</title>
<link rel="stylesheet" href="https://fonts.googleapis.com/css2?family=Fira+Sans:wght@300;400;600;700&display=swap">
<style>
  :root {
    --page: #ffffff;
    --ink: #231f20;
    --purple: #6b2364;
    --purple-deep: #421640;
    --purple-mid: #6a2565;
    --orange: #f7901e;
    --red: #ee4035;
    --white: #ffffff;
    --rule: #2b2b2b;
  }
  * { box-sizing: border-box; margin: 0; padding: 0; }
  html, body {
    width: 1200px;
    height: 776px;
    overflow: hidden;
    background: var(--page);
    font-family: "Fira Sans", Arial, sans-serif;
  }
  .sheet { position: relative; width: 1200px; height: 776px; }

  .card {
    position: absolute;
    width: 492px;
    height: 281px;
    overflow: hidden;
  }
  .card--front-a { left: 88px; top: 88px; border: 1px solid var(--rule); background: var(--white); }
  .card--front-b { left: 615px; top: 88px; border: 1px solid var(--rule); background: var(--white); }
  .card--back-a {
    left: 88px; top: 404px;
    background: linear-gradient(90deg, var(--purple-deep) 0%, var(--purple-mid) 50%, var(--purple-deep) 100%);
  }
  .card--back-b { left: 615px; top: 404px; background: var(--orange); }

  .wordmark {
    position: absolute;
    font-weight: 600;
    letter-spacing: -0.5px;
    line-height: 1;
    white-space: nowrap;
  }
  .card--front-a .wordmark { left: 24px; top: 113px; font-size: 50px; color: var(--purple); }
  .card--front-b .wordmark { right: 25px; top: 22px; font-size: 62px; color: var(--ink); }
  .card--back-a .wordmark {
    left: 0; right: 0; top: 107px; text-align: center;
    font-size: 66px; color: var(--white);
  }

  .line {
    position: absolute;
    font-size: 13.5px;
    font-weight: 300;
    line-height: 18px;
    white-space: nowrap;
  }
  .line--name { font-size: 17px; font-weight: 600; color: var(--orange); }
  .card--front-a .line { left: 279px; }
  .card--front-a .line:not(.line--name) { color: var(--purple); }
  .card--front-b .line { left: 207px; }
  .card--front-b .line:not(.line--name) { color: var(--ink); }

  .corner-square {
    position: absolute;
    width: 35px;
    height: 35px;
    background: var(--red);
  }
  .card--front-b .corner-square { left: 0; bottom: 0; }
  .card--back-b .corner-square { right: 0; bottom: 0; }

  .web-address {
    position: absolute;
    left: 0; right: 0; top: 120px;
    text-align: center;
    font-size: 21px;
    font-weight: 700;
    color: var(--white);
    text-shadow: 3px 5px 5px rgba(90, 50, 10, 0.55);
  }
</style>
</head>
<body>
<main class="sheet">

  <section class="card card--front-a" aria-label="Card front, layout A">
    <div class="wordmark">stepwise</div>
    <p class="line line--name" style="top:25px">First Last</p>
    <p class="line" style="top:43px">Title</p>
    <p class="line" style="top:140px">000-000-0000 Phone</p>
    <p class="line" style="top:158px">000-000-0000 Fax</p>
    <p class="line" style="top:175px">name@domainname.com</p>
    <p class="line" style="top:193px">www.domainname.com</p>
    <p class="line" style="top:224px">1234 Main Street</p>
    <p class="line" style="top:242px">Anytown, NN 00000</p>
  </section>

  <section class="card card--front-b" aria-label="Card front, layout B">
    <div class="wordmark">stepwise</div>
    <p class="line line--name" style="top:111px">First Last</p>
    <p class="line" style="top:128px">Title</p>
    <p class="line" style="top:157px">000-000-0000 Phone</p>
    <p class="line" style="top:175px">000-000-0000 Fax</p>
    <p class="line" style="top:192px">name@domainname.com</p>
    <p class="line" style="top:210px">www.domainname.com</p>
    <p class="line" style="top:239px">1234 Main Street, Anytown, NN 00000</p>
    <div class="corner-square"></div>
  </section>

  <section class="card card--back-a" aria-label="Card back, purple">
    <div class="wordmark">stepwise</div>
  </section>

  <section class="card card--back-b" aria-label="Card back, orange">
    <p class="web-address">www.domainname.com</p>
    <div class="corner-square"></div>
  </section>

</main>
</body>
</html>
```